Hip-Hop/Rap album needs artwork

I would like a design that parallels the ideas of beauty and flaws. My name is Varun Mehta and I'm titling it "Quiet Embers", this album is basically a collection of songs that have me trying to understand the good and evil in this world, how they run so close together at times. How they sometimes can be caused by the same source, or how sometimes we find beauty within all the ugliness we witness. Some subject matters include rape, serial killers, depression, the idea of love, the projection of women in the media, and the idea of dying prematurely.

Target Market(s)

Music listeners, who are looking for new music so artwork that will capture their eye and stand out, rough age estimate would be 17-35, people with time to kill.

Industry/Entity Type

Media

Font styles to use
Decorative
Script

Requirements
Must have
• please include my name VARUN MEHTA and the title QUIET EMBERS, preferably in different fonts

I'm going for something more moody and dark rather than something happy, so darker colors please.
Nice to have
• I would prefer to have a drawing or painting of some sort, to give some humanity to the design but not required.

```html
<!DOCTYPE html>
<html lang="en">
<head>
<meta charset="utf-8">
<title>Quiet Embers — Varun Mehta</title>
<link href="https://fonts.googleapis.com/css2?family=Cormorant+Garamond:ital,wght@1,300&family=Rubik+Dirt&display=swap" rel="stylesheet">
<style>
  :root {
    --stage: #d7d7d7;
    --night: #0b0605;
    --ember-deep: #8a1a05;
    --ember: #e2460c;
    --flame: #ff8a1e;
    --glow: #ffd46a;
    --ink-light: #ffffff;
  }
  html, body {
    margin: 0;
    padding: 0;
    width: 1200px;
    height: 1000px;
    overflow: hidden;
    background: var(--stage);
  }
  .canvas {
    position: relative;
    width: 1200px;
    height: 1000px;
    background: var(--stage);
  }
  .album-cover {
    position: absolute;
    left: 312px;
    top: 212px;
    width: 576px;
    height: 576px;
    overflow: hidden;
    background:
      radial-gradient(circle at 50% 48%, var(--flame) 0%, var(--ember) 30%, transparent 55%),
      radial-gradient(circle at 85% 30%, rgba(226,70,12,0.85) 0%, transparent 45%),
      radial-gradient(circle at 80% 90%, rgba(226,70,12,0.9) 0%, transparent 50%),
      linear-gradient(135deg, var(--night) 0%, var(--ember-deep) 45%, var(--ember) 75%, var(--night) 100%);
  }
  .cover-artwork {
    position: absolute;
    inset: 0;
    width: 100%;
    height: 100%;
  }
  .artist-name {
    position: absolute;
    top: 48px;
    left: 0;
    width: 100%;
    margin: 0;
    text-align: center;
    font-family: "Cormorant Garamond", serif;
    font-style: italic;
    font-weight: 300;
    font-size: 62px;
    letter-spacing: 1px;
    color: var(--ink-light);
    text-shadow: 0 0 6px rgba(0,0,0,0.35);
  }
  .album-title {
    position: absolute;
    top: 470px;
    left: 0;
    width: 100%;
    margin: 0;
    text-align: center;
    font-family: "Rubik Dirt", sans-serif;
    font-weight: 400;
    font-size: 50px;
    letter-spacing: 2px;
    color: var(--ink-light);
  }
</style>
</head>
<body>
  <main class="canvas">
    <section class="album-cover">
      <svg class="cover-artwork" viewBox="0 0 576 576" role="img" aria-label="Painted portrait of a woman inside a glowing ring of fire, surrounded by swirling embers and falling sparks">
        <defs>
          <radialGradient id="ring-glow" cx="50%" cy="50%" r="50%">
            <stop offset="0%" stop-color="#7a2a10"/>
            <stop offset="62%" stop-color="#b4400f"/>
            <stop offset="78%" stop-color="#ffd46a"/>
            <stop offset="86%" stop-color="#ff8a1e"/>
            <stop offset="100%" stop-color="#e2460c" stop-opacity="0"/>
          </radialGradient>
        </defs>
        <circle cx="288" cy="290" r="175" fill="url(#ring-glow)"/>
      </svg>
      <h2 class="artist-name">VARUN MEHTA</h2>
      <h1 class="album-title">QUIET EMBERS</h1>
    </section>
  </main>
</body>
</html>
```